Campaign Flyer for a local election

Black and white election flyer

See information below to be included:

Re-elect Morton
Experienced Glenmoor Board Member
Experienced NYC Principal
Experienced leader

One Year Board Accomplishments:
-Installed New Park Lights (Bollards)
-Red Brick Road Repair Project
-Established Closer Ties with Our local precinct to frequently monitor the community with directed security patrols. Requested an increased police presence.
-Met with the 82nd Precinct Officials & Assemblywoman, Linda Marwick to discuss our security issues
- Focused on maintenance of streetlights to make brighter streets
-Negotiated Contract & Hired Our New Landscaper, Hollowfield Landscapers
-Major Homeowner Shrub Replacement Project
- Addressing Standing Water in our Park (Installed French Drain)
- Replaced and upgraded all 5 outdoor circuit breaker panels
-Write monthly community newsletters
-Sewer cleaning project (had all community catch basins cleaned)
-Carefully overseeing our new school project. Coordinating with the sponsor and the school directors
-Delivered a very healthy budget to the community
-Works closely with our committees
-Events: Zoo event, Petting Zoo, Outdoor Movie Night, Egg Hunt

It is my intent to seek re-election.
(Photo) Morton Velasquez
-Dedicated to improving our community
-Hard-working…He gets thing done!
-Trustworthy

. .

Please note, I am submitting new information under accomplishments. The list of accomplishments should be in the same sequence, starting with: Met with the 82nd Precinct....
Please carefully review.
----------------------------------------------------------------------------------------------------------------------------------------------------------------

Re-elect Morton
Experienced NYC Principal
Experienced leader

Last Year’s Board Accomplishments:

-Met with the 82nd Precinct Officials & Assemblywoman, Linda Marwick, to discuss our security issues. Requested increased police presence.
-Established a strong partnership with the 82nd precinct to frequently monitor the community with directed security patrols.
-Replaced all new park lights (Bollards) to make the park brighter
- Focused on maintenance of streetlights to make streets brighter
-‘Fixing Our Streets Project’ (Repaired all cracked/missing red bricks)
-Homeowner Shrub Replacement Project (Replaced hundreds of bushes)
- I write the monthly community newsletter
-Carefully overseeing our new school project. Coordinating with the sponsor and the school director
-Monitoring C of O’s and homeowners Insurance

(Photo) Morton Velasquez
-Hard-working! I get things done!
-Trustworthy

. .

Re-elect Morton
Experienced NYC Principal
Experienced leader

(Photo) Morton Velasquez
-Trustworthy

. .

Target Market(s)

A Community electing a Board Member

Industry/Entity Type

residential election

Requirements
Must have
• all black, white and grey print. Flyers will not be printed in color
Nice to have
• See the information in the attachment below containing all my accomplishments
Should not have
• color

```html
<!DOCTYPE html>
<html lang="en">
<head>
<meta charset="utf-8">
<title>Re-elect Morton – Campaign Flyer</title>
<link rel="stylesheet" href="https://fonts.googleapis.com/css2?family=Oswald:wght@600&family=Fira+Sans:wght@400;500;600;700;800&display=swap">
<style>
  :root {
    --backdrop: #4d4d4d;
    --paper: #ffffff;
    --panel: #eeeeee;
    --headline: #5c5c5c;
    --ink: #222222;
    --ink-soft: #333333;
    --band: #6b6b6b;
    --bullet: #6a6a6a;
    --photo-light: #c9c9c9;
    --photo-dark: #3a3a3a;
  }
  * { box-sizing: border-box; margin: 0; padding: 0; }
  html, body { width: 1200px; height: 1200px; overflow: hidden; }
  body { background: var(--backdrop); position: relative; font-family: "Fira Sans", sans-serif; }

  .flyer {
    position: absolute; left: 178px; top: 5px;
    width: 843px; height: 1190px;
    background: var(--paper); overflow: hidden;
  }
  .accent-panel { position: absolute; left: 0; top: 280px; width: 843px; height: 655px; }
  .candidate-photo { position: absolute; left: 0; top: 0; width: 843px; height: 935px; }

  .headline {
    position: absolute; left: 46px; top: 38px;
    font-family: "Oswald", sans-serif; font-weight: 600;
    font-size: 84px; line-height: 1; letter-spacing: -0.5px;
    color: var(--headline); text-transform: uppercase;
  }
  .credentials {
    position: absolute; left: 48px; top: 140px;
    list-style: none;
    font-size: 31px; font-weight: 600; line-height: 41px; color: var(--ink-soft);
  }

  .accomplishments { position: absolute; left: 48px; top: 298px; }
  .accomplishments-title {
    font-size: 20.5px; font-weight: 700; color: var(--ink);
    text-transform: uppercase; margin-bottom: 7px;
  }
  .accomplishment-list { list-style: none; }
  .accomplishment {
    position: relative; padding-left: 20px;
    font-size: 14.6px; line-height: 19px; color: var(--ink);
    text-align: justify; margin-bottom: 6.2px; width: 420px;
  }
  .accomplishment svg { position: absolute; left: 2px; top: 4px; width: 11px; height: 11px; }

  .intent-band {
    position: absolute; left: 0; top: 935px; width: 843px; height: 62px;
    background: var(--band); color: var(--paper);
    font-size: 38px; font-weight: 800; letter-spacing: 0.2px;
    display: flex; align-items: center; justify-content: center;
    text-transform: uppercase;
  }

  .candidate-name {
    position: absolute; left: 48px; top: 1016px;
    font-family: "Oswald", sans-serif; font-weight: 600;
    font-size: 58px; line-height: 72px; color: var(--headline);
    text-transform: uppercase;
  }
  .qualities { position: absolute; left: 320px; top: 1032px; list-style: none; }
  .quality {
    display: flex; align-items: center; gap: 10px;
    height: 40px; font-size: 24.5px; font-weight: 600; color: var(--ink);
  }
  .quality svg { width: 22px; height: 22px; flex: none; }
  .quality-connector { position: absolute; left: 10px; top: 30px; }
</style>
</head>
<body>
  <main class="flyer">
    <svg class="accent-panel" viewBox="0 0 843 655" aria-hidden="true">
      <rect width="843" height="655" fill="var(--panel)"/>
    </svg>

    <svg class="candidate-photo" viewBox="0 0 843 935" role="img" aria-label="Portrait photo of candidate Morton Velasquez over a grey textured backdrop">
      <defs>
        <linearGradient id="photoTone" x1="0" y1="0" x2="0.4" y2="1">
          <stop offset="0" stop-color="var(--photo-light)"/>
          <stop offset="0.55" stop-color="#8a8a8a"/>
          <stop offset="1" stop-color="var(--photo-dark)"/>
        </linearGradient>
      </defs>
      <polygon points="675,0 843,0 843,935 535,935 385,655" fill="url(#photoTone)"/>
      <polyline points="675,0 385,655 535,935" fill="none" stroke="#ffffff" stroke-width="3"/>
    </svg>

    <h1 class="headline">Re-elect Morton</h1>
    <ul class="credentials">
      <li>Experienced Glenmoor Board Member</li>
      <li>Experienced NYC Principal</li>
      <li>Experienced leader</li>
    </ul>

    <section class="accomplishments">
      <h2 class="accomplishments-title">One Year Board Accomplishments:</h2>
      <svg width="0" height="0" style="position:absolute">
        <symbol id="tick-bullet" viewBox="0 0 12 12">
          <circle cx="6" cy="6" r="6" fill="var(--bullet)"/>
          <path d="M3.3 6.2 L5.2 8 L8.8 4.2" fill="none" stroke="#fff" stroke-width="1.5"/>
        </symbol>
      </svg>
      <ul class="accomplishment-list">
        <li class="accomplishment"><svg><use href="#tick-bullet"/></svg>Installed New Park Lights (Bollards)</li>
        <li class="accomplishment"><svg><use href="#tick-bullet"/></svg>Red Brick Road Repair Project</li>
        <li class="accomplishment" style="width:412px"><svg><use href="#tick-bullet"/></svg>Established Closer Ties with Our local precinct to frequently monitor the community with directed security patrols. Requested an increased police presence.</li>
        <li class="accomplishment" style="width:400px;text-align:left"><svg><use href="#tick-bullet"/></svg>Met with the 82nd Precinct Officials &amp; Assemblywoman, Linda Marwick to discuss our security issues</li>
        <li class="accomplishment" style="width:365px"><svg><use href="#tick-bullet"/></svg>Focused on maintenance of streetlights to make brighter streets</li>
        <li class="accomplishment" style="width:345px"><svg><use href="#tick-bullet"/></svg>Negotiated Contract and Hired Our New Landscaper, Hollowfield Landscapers</li>
        <li class="accomplishment" style="width:340px"><svg><use href="#tick-bullet"/></svg>Major Homeowner Shrub Replacement Project</li>
        <li class="accomplishment" style="width:315px"><svg><use href="#tick-bullet"/></svg>Addressing Standing Water in our Park (Installed French Drain)</li>
        <li class="accomplishment" style="width:300px"><svg><use href="#tick-bullet"/></svg>Replaced and upgraded all 5 outdoor circuit breaker panels</li>
        <li class="accomplishment" style="width:330px"><svg><use href="#tick-bullet"/></svg>Write monthly community newsletters</li>
        <li class="accomplishment" style="width:335px"><svg><use href="#tick-bullet"/></svg>Sewer cleaning project (had all community catch basins cleaned)</li>
        <li class="accomplishment" style="width:367px"><svg><use href="#tick-bullet"/></svg>Carefully overseeing our new school project. Coordinating with the sponsor and the school directors</li>
        <li class="accomplishment" style="width:400px"><svg><use href="#tick-bullet"/></svg>Delivered a very healthy budget to the community</li>
        <li class="accomplishment" style="width:410px"><svg><use href="#tick-bullet"/></svg>Works closely with our committees</li>
        <li class="accomplishment" style="width:422px;text-align:left"><svg><use href="#tick-bullet"/></svg>Events: Zoo event, Petting Zoo, Outdoor Movie Night, Egg Hunt</li>
      </ul>
    </section>

    <div class="intent-band">It is my intent to seek re-election</div>

    <h2 class="candidate-name">Morton<br>Velasquez</h2>

    <svg width="0" height="0" style="position:absolute">
      <symbol id="tick-ring" viewBox="0 0 22 22">
        <circle cx="11" cy="11" r="8.5" fill="#fff" stroke="var(--bullet)" stroke-width="2"/>
        <path d="M6.5 11 L10 14.3 L17 6.5" fill="none" stroke="var(--bullet)" stroke-width="2.2"/>
      </symbol>
    </svg>
    <ul class="qualities">
      <svg class="quality-connector" width="2" height="62" aria-hidden="true">
        <line x1="1" y1="0" x2="1" y2="62" stroke="var(--bullet)" stroke-width="1.5" stroke-dasharray="2 3"/>
      </svg>
      <li class="quality"><svg><use href="#tick-ring"/></svg>Dedicated to improving our community</li>
      <li class="quality"><svg><use href="#tick-ring"/></svg>Hard-working...He gets thing done!</li>
      <li class="quality"><svg><use href="#tick-ring"/></svg>Trustworthy</li>
    </ul>
  </main>
</body>
</html>
```